Bref créative
Stationary for Visual Explanation Business
Bus Card, Stationary
Professional
Martin Pelloway
CEO & Founder
487 E 29th Street, Suite 4B
New York, NY 10027
USA
martin@lumbrivista.com
www.lumbrivista.com
Looking for clean and modern sophisticated look and feel for a marketing service business company that offers visual explanations for technology companies. Not cutesy. A blend of QXR combined with creative agency.
The letterhead will serve as my proposal template. I will use it for placing text and illustrations.
I want to keep with the orange and gray of the logo.
I wil supply the AI version of the logo shortly.
Logo AI File with tagline and name
Logo Ai File with company name and no tagline
Logo Ai file with no tagline and no company name

```html
<!DOCTYPE html>
<html lang="en">
<head>
<meta charset="utf-8">
<title>Lumbri Vista Stationery</title>
<link href="https://fonts.googleapis.com/css2?family=Arimo:wght@400;700&display=swap" rel="stylesheet">
<style>
  :root {
    --orange: #f39325;
    --gray: #6b6d70;
    --gray-dark: #58595b;
    --paper: #ffffff;
    --frame: #dcdcdc;
    --shadow: rgba(0, 0, 0, 0.45);
    --text: #444446;
  }
  * { box-sizing: border-box; margin: 0; padding: 0; }
  html, body {
    width: 1200px; height: 743px; overflow: hidden;
    background: var(--paper);
    font-family: "Arimo", Arial, sans-serif;
    color: var(--text);
  }
  .canvas { position: relative; width: 1200px; height: 743px; }
  .presentation-frame {
    position: absolute; left: 19px; top: 29px; width: 1162px; height: 681px;
    border: 1px solid var(--frame);
  }
  .sheet {
    position: absolute; background: var(--paper);
    box-shadow: 6px 8px 12px var(--shadow);
  }

  /* brand wordmark */
  .brand-name {
    position: absolute; color: var(--gray); font-weight: 400;
    letter-spacing: -0.02em; line-height: 1; white-space: nowrap;
  }
  .brand-tagline {
    position: absolute; color: var(--orange); white-space: nowrap; letter-spacing: 0.02em;
  }

  /* stripe bars */
  .stripe { position: absolute; display: flex; gap: 4px; }
  .stripe span { background: var(--gray-dark); height: 100%; display: block; }

  /* letterhead */
  .letterhead { left: 569px; top: 53px; width: 357px; height: 624px; }
  .letterhead .brand-name { left: 20px; top: 45px; font-size: 21px; }
  .letterhead .brand-tagline { left: 21px; top: 70px; font-size: 5.5px; }
  .letterhead .top-stripe { left: 74px; top: 5px; width: 276px; height: 10px; }
  .letterhead .bottom-stripe { left: 0; top: 607px; width: 357px; height: 10px; }
  .letterhead-footer {
    position: absolute; left: 0; right: 0; top: 578px; text-align: center;
    font-size: 7.5px; color: var(--text); white-space: nowrap;
  }

  /* envelope */
  .envelope { left: 41px; top: 336px; width: 540px; height: 230px; z-index: 2; }
  .envelope .brand-name { left: 18px; top: 22px; font-size: 21px; }
  .envelope .brand-tagline { left: 19px; top: 47px; font-size: 5.5px; }
  .return-address {
    position: absolute; left: 18px; top: 60px; font-size: 7.5px; line-height: 1.35;
    font-style: normal;
  }

  /* business card */
  .business-card { left: 943px; top: 211px; width: 226px; height: 111px; }
  .business-card .top-stripe { left: 6px; top: 4px; width: 214px; height: 8px; }
  .business-card .bottom-stripe { left: 6px; top: 99px; width: 214px; height: 8px; }
  .business-card .brand-name { left: 10px; top: 42px; font-size: 12px; }
  .business-card .brand-tagline { left: 10px; top: 57px; font-size: 3.5px; }
  .card-contact { position: absolute; left: 120px; top: 22px; font-size: 5.5px; line-height: 1.3; }
  .card-name { color: var(--orange); font-weight: 700; font-size: 7.5px; }
  .card-title { color: var(--orange); margin-bottom: 3px; }
</style>
</head>
<body>
<div class="canvas">
  <div class="presentation-frame"></div>

  <section class="sheet letterhead">
    <div class="stripe top-stripe">
      <span style="width:22px"></span><span style="width:22px"></span><span style="width:10px"></span>
      <span style="width:28px"></span><span style="width:22px"></span><span style="width:40px"></span>
      <span style="width:18px"></span><span style="width:60px"></span><span style="width:30px"></span>
    </div>
    <div class="brand-name">LumbriVista</div>
    <div class="brand-tagline">Visual explanations for technology</div>
    <p class="letterhead-footer">487 E 29th Street, Suite 4B, New York, NY 10027 • Phone: (212) 555-0148 • www.lumbrivista.com</p>
    <div class="stripe bottom-stripe">
      <span style="width:283px"></span><span style="width:20px"></span>
      <span style="width:20px"></span><span style="width:22px"></span>
    </div>
  </section>

  <section class="sheet envelope">
    <div class="brand-name">LumbriVista</div>
    <div class="brand-tagline">Visual explanations for technology</div>
    <address class="return-address">
      487 E 29th Street, Suite 4B<br>New York, NY 10027
    </address>
  </section>

  <section class="sheet business-card">
    <div class="stripe top-stripe">
      <span style="width:10px"></span><span style="width:10px"></span><span style="width:10px"></span>
      <span style="width:10px"></span><span style="width:162px"></span>
    </div>
    <div class="brand-name">LumbriVista</div>
    <div class="brand-tagline">Visual explanations for technology</div>
    <div class="card-contact">
      <div class="card-name">Martin Pelloway</div>
      <div class="card-title">CEO &amp; Founder</div>
      <div>487 E 29th Street, Suite 4B</div>
      <div>New York, NY 10027</div>
      <div>Phone: (212) 555-0148</div>
      <div>martin@lumbrivista.com</div>
      <div>www.lumbrivista.com</div>
    </div>
    <div class="stripe bottom-stripe">
      <span style="width:152px"></span><span style="width:12px"></span><span style="width:12px"></span>
      <span style="width:12px"></span><span style="width:14px"></span>
    </div>
  </section>
</div>
</body>
</html>
```